Startup Biz for Seniors needs your help!

Our business is a Startup that Employs Caregivers to do IN HOME Care of the Elderly. Our website is not yet running. But, a business similar to ours is Tallbrookcare.com

We are looking for a card that only has 4 Elements:
-Logo
- Website
- Tag Line
- Phone
We would like to see some eye catching backgrounds.
We would like to see some designs with and some without a Photo.
Would like the Photo to be of a Caregiver taking care of a Senior. The photo should show both of them smiling.

Target Market(s)

Age 35-55 who has Parents that are Elderly and need care

Industry/Entity Type

Home Health Care

Contact Information for Business Card

Want it to Pop Out to the viewer . Thinking maybe:
Side 1: LOGO with Website & Tag line
Side 2: Phone Number

Font styles to use
Other font styles liked:
• Same Font as our Logo

Colors

Designer to choose colors to be used in the design.

Requirements
Must have
• Logo, website, Tag Line, Phone number and Email: "info@velvetdays.example"
• Please use one of the photos that I have attached.
Nice to have
• Would like to see a Photo worked in that has a Care Taker taking care of an Elderly Person and they are both smiling.

```html
<!DOCTYPE html>
<html lang="en">
<head>
<meta charset="utf-8">
<title>VelvetDays business card</title>
<link rel="stylesheet" href="https://fonts.googleapis.com/css2?family=Roboto:wght@500;700&family=Kaushan+Script&display=swap">
<style>
  :root {
    --backdrop: #e9eaeb;
    --card: #f6f6f6;
    --orange: #d95f3a;
    --blue: #4a5ea6;
    --ink-grey: #555a5e;
    --photo-light: #d9d4cc;
    --photo-mid: #b9ada1;
    --photo-dark: #8f9a90;
  }
  html, body {
    margin: 0;
    width: 1200px;
    height: 969px;
    overflow: hidden;
    background: var(--backdrop);
  }
  .stage {
    position: relative;
    width: 1200px;
    height: 969px;
  }
  .card {
    position: absolute;
    left: 320px;
    width: 560px;
    height: 320px;
    background: var(--card);
    box-shadow: 0 6px 18px rgba(0,0,0,0.15);
    overflow: hidden;
  }
  .card--front { top: 120px; }
  .card--back { top: 520px; }
  .card svg { display: block; }
  .brand-vertical {
    font-family: "Roboto", sans-serif;
    font-weight: 700;
    font-size: 34px;
    fill: var(--blue);
  }
  .brand-name {
    font-family: "Roboto", sans-serif;
    font-weight: 700;
    font-size: 28px;
    fill: var(--blue);
  }
  .tag-line {
    font-family: "Kaushan Script", cursive;
    font-size: 34px;
    fill: var(--ink-grey);
  }
  .phone-number {
    font-family: "Roboto", sans-serif;
    font-weight: 700;
    font-size: 29px;
    fill: var(--blue);
  }
  .website,
  .email {
    font-family: "Roboto", sans-serif;
    font-weight: 500;
    font-size: 24px;
    fill: var(--blue);
  }
</style>
</head>
<body>
<main class="stage">

  <!-- Side 1 -->
  <section class="card card--front" aria-label="Card front">
    <svg width="560" height="320" viewBox="0 0 560 320">
      <defs>
        <linearGradient id="photo-front" x1="0" y1="0" x2="1" y2="1">
          <stop offset="0" stop-color="var(--photo-dark)"/>
          <stop offset="0.5" stop-color="var(--photo-light)"/>
          <stop offset="1" stop-color="var(--photo-mid)"/>
        </linearGradient>
      </defs>
      <polygon class="photo" role="img" aria-label="Photo of a smiling caregiver hugging a smiling elderly woman"
        points="104,0 560,0 560,320 200,320 224,165" fill="url(#photo-front)"/>
      <polygon class="band-blue" points="68,0 80,0 200,165 176,320 164,320 188,165" fill="var(--blue)"/>
      <polygon class="band-orange" points="80,0 104,0 224,165 200,320 176,320 200,165" fill="var(--orange)"/>
      <circle class="brand-dot" cx="190" cy="165" r="44" fill="var(--orange)" stroke="var(--card)" stroke-width="4"/>
      <text class="brand-vertical" transform="translate(30,40) rotate(90)">VelvetDays</text>
    </svg>
  </section>

  <!-- Side 2 -->
  <section class="card card--back" aria-label="Card back">
    <svg width="560" height="320" viewBox="0 0 560 320">
      <defs>
        <linearGradient id="photo-back" x1="0" y1="0" x2="1" y2="1">
          <stop offset="0" stop-color="var(--photo-dark)"/>
          <stop offset="0.45" stop-color="var(--photo-light)"/>
          <stop offset="1" stop-color="var(--photo-mid)"/>
        </linearGradient>
      </defs>
      <polygon class="photo" role="img" aria-label="Photo of a smiling caregiver"
        points="0,0 175,0 160,190 200,320 0,320" fill="url(#photo-back)"/>
      <polygon class="band-orange" points="175,0 199,0 184,190 224,320 200,320 160,190" fill="var(--orange)"/>
      <polygon class="band-blue" points="199,0 209,0 194,190 234,320 224,320 184,190" fill="var(--blue)"/>

      <circle class="brand-dot" cx="255" cy="40" r="14" fill="var(--orange)"/>
      <text class="brand-name" x="276" y="50">VelvetDays</text>
      <text class="tag-line" x="292" y="100">Your Tag Line</text>

      <g class="contact contact--phone">
        <circle cx="214" cy="188" r="18" fill="var(--blue)"/>
        <path d="M206,180 q2,-3 5,-1 l3,4 q1,2 -1,3 l-2,1 q2,5 7,7 l1,-2 q1,-2 3,-1 l4,3 q2,3 -1,5 q-3,3 -7,1 q-11,-5 -14,-15 q-1,-3 2,-5 z" fill="none" stroke="#fff" stroke-width="2"/>
        <text class="phone-number" x="246" y="198">+00 123 456 789</text>
      </g>

      <g class="contact contact--web">
        <circle cx="228" cy="238" r="18" fill="var(--blue)"/>
        <g fill="none" stroke="#fff" stroke-width="1.8">
          <circle cx="228" cy="238" r="10"/>
          <ellipse cx="228" cy="238" rx="4.5" ry="10"/>
          <line x1="218" y1="238" x2="238" y2="238"/>
          <line x1="220" y1="232" x2="236" y2="232"/>
          <line x1="220" y1="244" x2="236" y2="244"/>
        </g>
        <text class="website" x="260" y="246">VelvetDays.example</text>
      </g>

      <g class="contact contact--email">
        <circle cx="244" cy="284" r="18" fill="var(--blue)"/>
        <g fill="none" stroke="#fff" stroke-width="1.8">
          <rect x="234" y="277" width="20" height="14" rx="1.5"/>
          <polyline points="234,278 244,286 254,278"/>
        </g>
        <text class="email" x="276" y="292">info@velvetdays.example</text>
      </g>
    </svg>
  </section>

</main>
</body>
</html>
```